Business card for my new company (Accounting firm)

I need a business card for my new business Corvel Advisory and Finance SA. Our services are accounting, tax, audit and financial management. Our customers are small companies, start-ups and new companies. The final design has to show financial security, trust and growth. Please find our logo attached to the business card. Text for the business card: Corvel Advisory and Finance SA Tomas de Valbueno Director and Founder Certified Accountant Tel. 022 418 27 53 tv@corvelconseil.ch www.corvelconseil.ch Rue des Verniquets 14 1201 Geneva
Target Market(s)
Our customers are small companies, start-ups and new companies.
Industry/Entity Type
Finance And Accounting
Contact Information for Business Card
Corvel Conseil et Finance SA
Tomas de Valbueno
Directeur et Fondateur
Expert-comptable diplômé
Tél. 022 418 27 53
tv@corvelconseil.ch
www.corvelconseil.ch
Rue des Verniquets 14
1201 Genève

```html
<!DOCTYPE html>
<html lang="fr">
<head>
<meta charset="utf-8">
<title>Corvel Conseil et Finance SA – Carte de visite</title>
<link rel="stylesheet" href="https://fonts.googleapis.com/css2?family=Lato:wght@400;700&display=swap">
<style>
  :root {
    --backdrop: #121315;
    --card: #1c1d20;
    --cyan: #2aaee2;
    --deep-blue: #1a6aa0;
    --ink: #f2f4f6;
  }
  * { box-sizing: border-box; margin: 0; padding: 0; }
  html, body {
    width: 1200px; height: 912px; overflow: hidden;
    background: var(--backdrop);
    font-family: "Lato", sans-serif;
    color: var(--ink);
  }
  .stage {
    width: 1200px; height: 912px;
    display: flex; flex-direction: column; align-items: center; justify-content: center;
    gap: 32px;
  }
  .card {
    position: relative;
    width: 700px; height: 400px;
    background: var(--card);
    overflow: hidden;
  }
  /* Front */
  .card-front { display: flex; align-items: center; justify-content: center; }
  .brand { display: flex; align-items: center; gap: 16px; }
  .brand-square { width: 34px; height: 34px; background: var(--cyan); }
  .brand-name { font-weight: 700; color: var(--ink); letter-spacing: 0.5px; }
  .card-front .brand-name { font-size: 34px; }

  /* Back */
  .card-back .brand { position: absolute; left: 60px; top: 164px; gap: 12px; }
  .card-back .brand-square { width: 24px; height: 24px; }
  .card-back .brand-name { font-size: 22px; }

  .holder { position: absolute; right: 48px; top: 70px; text-align: right; }
  .holder-name { color: var(--cyan); font-weight: 700; font-size: 27px; line-height: 1.15; }
  .holder-role { font-size: 16px; line-height: 1.4; }

  .divider {
    position: absolute; left: 120px; right: 40px; top: 210px;
    height: 1px; background: var(--cyan);
  }

  .address {
    position: absolute; right: 48px; top: 228px; text-align: right;
    font-size: 16px; line-height: 1.35; font-style: normal;
  }

  .contact {
    position: absolute; left: 70px; top: 262px;
    list-style: none; font-size: 19px; line-height: 1.5;
  }
  .contact li { display: flex; align-items: center; gap: 12px; }
  .contact svg { width: 18px; height: 18px; fill: var(--cyan); flex: none; }

  .accent-area {
    position: absolute; right: 0; bottom: 0;
    width: 320px; height: 52px;
    background: linear-gradient(90deg, var(--cyan), var(--deep-blue));
  }
  .website {
    position: absolute; right: 36px; bottom: 16px;
    font-size: 16px; color: var(--ink);
  }
</style>
</head>
<body>
<main class="stage">
  <section class="card card-front" aria-label="Recto">
    <div class="brand">
      <span class="brand-square"></span>
      <span class="brand-name">Corvel Conseil et Finance</span>
    </div>
  </section>

  <section class="card card-back" aria-label="Verso">
    <div class="accent-area" role="img" aria-label="Decorative blue accent area"></div>

    <div class="brand">
      <span class="brand-square"></span>
      <span class="brand-name">Corvel Conseil et Finance</span>
    </div>

    <div class="holder">
      <p class="holder-name">Tomas de Valbueno</p>
      <p class="holder-role">Directeur et Fondateur</p>
      <p class="holder-role">Expert-comptable diplômé</p>
    </div>

    <div class="divider"></div>

    <address class="address">
      Corvel Conseil et Finance SA<br>
      Rue des Verniquets 14<br>
      1201 Genève
    </address>

    <ul class="contact">
      <li>
        <svg viewBox="0 0 24 24" aria-hidden="true"><path d="M6.6 10.8a15.1 15.1 0 0 0 6.6 6.6l2.2-2.2a1 1 0 0 1 1-.25 11.4 11.4 0 0 0 3.6.57 1 1 0 0 1 1 1V20a1 1 0 0 1-1 1A17 17 0 0 1 3 4a1 1 0 0 1 1-1h3.5a1 1 0 0 1 1 1c0 1.25.2 2.45.57 3.57a1 1 0 0 1-.25 1z"/></svg>
        <span>022 418 27 53</span>
      </li>
      <li>
        <svg viewBox="0 0 24 24" aria-hidden="true"><path d="M2 5h20v14H2z"/><path d="M2 5l10 8 10-8" fill="none" stroke="var(--card)" stroke-width="1.6"/></svg>
        <span>tv@corvelconseil.ch</span>
      </li>
    </ul>

    <p class="website">www.corvelconseil.ch</p>
  </section>
</main>
</body>
</html>
```